eBook Cover

Here is the book title: 27 LESSONS EACH MINISTER SHOULD
LEARN ABOUT FINANCES

Here is the subtitle (or author section): A Harvest Lantern eBook

I've attached the harvest lantern logo below.

Target Market(s)

Church Pastors

Requirements
Must have
• Lantern Logo and Harvest Lantern color palette.
Nice to have
• I have attached some sample book covers that I like

```html
<!DOCTYPE html>
<html lang="en">
<head>
<meta charset="utf-8">
<title>27 Lessons Each Minister Should Learn About Finances — eBook Cover</title>
<link rel="stylesheet" href="https://fonts.googleapis.com/css2?family=Comfortaa:wght@700&family=Montserrat:wght@500&family=Patua+One&display=swap">
<style>
  :root {
    --bg-center: #2f6073;
    --bg-mid: #244b5c;
    --bg-edge: #17323f;
    --white: #ffffff;
    --mint: #86e3c8;
    --yellow: #f6e45c;
    --brand-green: #5ccf8c;
  }
  html, body {
    margin: 0;
    padding: 0;
    overflow: hidden;
    background: var(--bg-edge);
  }
  .cover {
    position: relative;
    width: 865px;
    height: 1200px;
    overflow: hidden;
    background: radial-gradient(ellipse 75% 60% at 50% 42%, var(--bg-center) 0%, var(--bg-mid) 55%, var(--bg-edge) 100%);
    font-family: "Comfortaa", sans-serif;
    color: var(--white);
  }
  .series {
    position: absolute;
    top: 36px;
    left: 0;
    right: 0;
    margin: 0;
    text-align: center;
    font-family: "Montserrat", sans-serif;
    font-weight: 500;
    font-size: 27px;
    letter-spacing: 5px;
    text-transform: uppercase;
  }
  .title {
    position: absolute;
    top: 385px;
    left: 78px;
    display: flex;
    align-items: flex-start;
    margin: 0;
    font-weight: 700;
    line-height: 1;
  }
  .title-number {
    font-size: 172px;
    letter-spacing: -6px;
    margin-right: 12px;
    margin-top: 2px;
  }
  .title-words {
    display: flex;
    flex-direction: column;
  }
  .line { display: flex; align-items: baseline; }
  .word-large { font-size: 68px; }
  .word-small { font-size: 28px; margin-left: 10px; }
  .word-small.lead { margin-left: 0; margin-right: 10px; }
  .accent { color: var(--mint); }
  .word-hero { font-size: 84px; color: var(--mint); margin-top: 4px; letter-spacing: -1px; }
  .line-learn { margin-top: 8px; }
  .word-closing {
    font-family: "Patua One", serif;
    font-weight: 400;
    font-size: 92px;
    color: var(--yellow);
    margin-top: 6px;
    letter-spacing: 1px;
  }
  .publisher {
    position: absolute;
    bottom: 70px;
    left: 0;
    right: 0;
    display: flex;
    justify-content: center;
    align-items: center;
    gap: 12px;
    color: var(--brand-green);
    font-weight: 700;
    font-size: 30px;
    text-transform: uppercase;
  }
  .publisher-dot {
    width: 20px;
    height: 20px;
    border-radius: 50%;
    background: var(--brand-green);
  }
</style>
</head>
<body>
  <main class="cover">
    <p class="series">A Harvest Lantern eBook</p>

    <h1 class="title">
      <span class="title-number">27</span>
      <span class="title-words">
        <span class="line">
          <span class="word-large">LESSONS</span>
          <span class="word-small accent">EACH</span>
        </span>
        <span class="word-hero">MINISTER</span>
        <span class="line line-learn">
          <span class="word-small lead">SHOULD</span>
          <span class="word-large">LEARN</span>
          <span class="word-small">ABOUT</span>
        </span>
        <span class="word-closing">FINANCES</span>
      </span>
    </h1>

    <footer class="publisher">
      <span class="publisher-dot"></span>
      <span class="publisher-name">The Lantern Company</span>
    </footer>
  </main>
</body>
</html>
```